Pediatric Occupational Therapy Brochure Design

This design really needs to stand out, especially with all the wordage that I have included. These brochures will be given to doctors, future clients, and caregivers. I have included the logo on by brochure, so incorporating the same or similar colors would be fantastic. A trifold brochure would probably be best to fit all the information, as this is a new business and needs to convey all the information in a way that people will read.

Target Market(s)

Doctor's offices and caregivers of children with disabilities.

Industry/Entity Type

Health Care

Font styles to use
Serif
Sans Serif

Colors
33a6d7
85acd3
ffffff
33b8a4
86cfc7

Requirements
Must have
• I would like the same colors of the logo incorporated in the brochure design.
Nice to have
• I would like to see the butterfly somehow in the background or used in the design. Also a trifold or two page design would be greatly appreciated as long as the information can fit.

```html
<!DOCTYPE html>
<html lang="en">
<head>
<meta charset="utf-8">
<title>Willow Lane Therapy – Pediatric Occupational Therapy Brochure</title>
<link href="https://fonts.googleapis.com/css2?family=Libre+Baskerville:wght@400;700&family=Questrial&display=swap" rel="stylesheet">
<style>
  :root{
    --teal:#2b9c9e;
    --teal-dark:#1f8587;
    --aqua:#7dcfcc;
    --aqua-soft:#a9e0dd;
    --grey:#5f6062;
    --grey-band:#8a8b8d;
    --ink:#2c2c2c;
    --paper:#ffffff;
    --backdrop:#3a3a3a;
    --serif:'Libre Baskerville', Georgia, serif;
    --sans:'Questrial', Arial, sans-serif;
  }
  *{box-sizing:border-box;margin:0;padding:0}
  html,body{width:1200px;height:899px;overflow:hidden;background:var(--backdrop)}
  .brochure{position:absolute;left:30px;top:20px;width:1140px;height:859px;display:flex}
  .panel{position:relative;width:380px;height:859px;background:var(--paper);overflow:hidden}
  .panel + .panel{border-left:1px solid #e3e3e3}
  .wave{position:absolute;left:0;width:380px}

  /* services panel */
  .services-tab{position:absolute;left:0;top:52px;width:345px;height:52px;background:var(--teal);
    border-radius:0 14px 14px 0;color:#fff;font-family:var(--sans);font-size:21px;
    line-height:52px;padding-left:24px;box-shadow:0 4px 4px rgba(0,0,0,.25);white-space:nowrap}
  .service-list{position:absolute;left:36px;top:132px;list-style:none}
  .service-list li{font-family:var(--serif);font-size:15.5px;color:var(--ink);height:37.5px;
    display:flex;align-items:center;gap:14px;white-space:nowrap}
  .service-list li::before{content:"";width:12px;height:12px;border-radius:50%;background:var(--aqua);flex:none}
  .panel-title{position:absolute;left:34px;color:#fff;font-family:var(--sans)}
  .panel-title h2{font-size:23px;font-weight:400;line-height:1.2}
  .panel-title p{font-size:17px;margin-top:2px}

  /* middle panel */
  .get-started{position:absolute;left:30px;right:30px;top:60px;text-align:center}
  .get-started h3{font-family:var(--sans);color:var(--teal);font-size:20px;font-weight:400;margin-bottom:10px}
  .get-started p{font-family:var(--serif);font-size:13px;line-height:1.5;color:var(--ink);text-align:justify;text-align-last:center}
  .info{position:absolute;left:0;right:0;text-align:center;font-family:var(--sans)}
  .info h4{color:var(--teal);font-size:20px;font-weight:400}
  .info span{display:block;color:var(--ink);font-size:19px;margin-top:4px}
  .child-photo{position:absolute;left:34px;top:395px;width:100px;height:230px;border-radius:40px 40px 10px 10px;
    background:linear-gradient(180deg,#e9d8c6 0%,#f4f4f4 30%,#dfe7ee 70%,#9eb6cf 100%)}
  .brand-mark{display:flex;align-items:center;gap:10px;font-family:var(--sans);color:var(--grey);white-space:nowrap}
  .brand-mark i{width:34px;height:34px;border-radius:50%;background:var(--aqua);flex:none}
  .brand-mark.mid{position:absolute;left:148px;top:490px;font-size:18px}
  .brand-mark.mid i{width:28px;height:28px}
  .contact-card{position:absolute;left:30px;top:640px;width:300px;height:125px;background:var(--aqua);
    border-radius:14px;padding:16px 20px;font-family:var(--serif);color:var(--ink);box-shadow:0 5px 8px rgba(0,0,0,.3)}
  .contact-card h5{font-size:17px;margin-bottom:8px;font-weight:700;white-space:nowrap}
  .contact-card div{font-size:11.5px;display:flex;align-items:center;gap:8px;margin-top:5px;white-space:nowrap}
  .contact-card svg{width:11px;height:11px;fill:#fff;flex:none}

  /* cover panel */
  .brand-mark.cover{position:absolute;left:30px;top:50px;font-size:28px}
  .brand-mark.cover i{width:48px;height:48px}
  .cover-photo{position:absolute;left:40px;top:225px;width:320px;height:320px;border-radius:50%;
    background:linear-gradient(135deg,#dfe6ef 0%,#f1d9c4 40%,#6f8fd0 75%,#ffffff 100%);
    border:10px solid var(--aqua)}
  .title-pill{position:absolute;left:20px;top:585px;width:345px;height:108px;background:var(--teal);
    border-radius:20px;color:#fff;text-align:center;font-family:var(--sans);padding-top:14px;
    box-shadow:0 5px 6px rgba(0,0,0,.3)}
  .title-pill h1{font-size:24px;font-weight:400;line-height:1.2}
  .title-pill p{font-size:18px;margin-top:2px}
  .cover-contact{position:absolute;right:28px;top:728px;text-align:right;font-family:var(--sans);color:var(--ink);font-size:16px;line-height:1.6;white-space:nowrap}
  .cover-contact strong{color:var(--teal);font-weight:400;font-size:17px}
</style>
</head>
<body>
<main class="brochure">

  <section class="panel services">
    <div class="services-tab">Services Offered for Your Child</div>
    <ul class="service-list">
      <li>Social Skills</li>
      <li>Oral Motor</li>
      <li>Sensory Activities</li>
      <li>Feeding</li>
      <li>Handling Techniques</li>
      <li>Handwriting</li>
      <li>Home Exercise Program</li>
      <li>Kinesiotaping</li>
      <li>Sound-Based Listening Therapy</li>
      <li>Neuro-Developmental Treatment</li>
      <li>Patient/Parent Education</li>
      <li>Postural Reeducation</li>
      <li>Sensory Integration</li>
      <li>Therapeutic play</li>
      <li>...and much more!</li>
    </ul>
    <svg class="wave" style="top:700px" height="159" viewBox="0 0 380 159">
      <path d="M0 60 Q190 0 380 10 L380 159 L0 159Z" fill="var(--teal)"/>
      <path d="M0 60 Q190 0 380 10 L380 0 Q190 -6 0 50Z" fill="var(--aqua)"/>
    </svg>
    <div class="panel-title" style="top:770px">
      <h2>Pediatric Occupational<br>Therapy Services</h2>
      <p>(In home services)</p>
    </div>
  </section>

  <section class="panel middle">
    <div class="get-started">
      <h3>How to get started!</h3>
      <p>If you or someone you know has concerns about their child’s development, discuss with your doctor the concern and request a prescription for an occupational therapy evaluation.</p>
    </div>
    <div class="info" style="top:225px">
      <h4>To schedule an appointment,</h4>
      <span>call (555) 014-2298</span>
    </div>
    <div class="info" style="top:305px">
      <h4>Business Hours:</h4>
      <span>Monday-Saturday</span>
      <span>8:00am-7:00pm</span>
    </div>
    <div class="child-photo" role="img" aria-label="Photo of a smiling young boy in a doctor's coat giving a thumbs up"></div>
    <div class="brand-mark mid"><i></i>Willow Lane Therapy</div>
    <svg class="wave" style="top:600px" height="259" viewBox="0 0 380 259">
      <path d="M0 70 Q200 110 380 0 L380 259 L0 259Z" fill="var(--grey-band)"/>
      <path d="M0 70 Q200 110 380 0 L380 -20 Q200 80 0 50Z" fill="var(--teal)"/>
    </svg>
    <div class="contact-card">
      <h5>Willow Lane Therapy, LLC</h5>
      <div><svg viewBox="0 0 10 10"><path d="M5 0 L10 5 H8.5 V10 H1.5 V5 H0Z"/></svg>48 Maple Ave, Riverton, Texas 78000</div>
      <div><svg viewBox="0 0 10 10"><path d="M2 0 L4 2.5 L3 4 Q4 6 6 7 L7.5 6 L10 8 L8.5 10 Q3 9.5 0 1.5Z"/></svg>(555) 014-2298</div>
      <div><svg viewBox="0 0 10 10"><path d="M0 2 H10 V8 H0Z M0 2 L5 6 L10 2" stroke="#7dcfcc" stroke-width=".8"/></svg>hello@willowlanetherapy.com</div>
    </div>
  </section>

  <section class="panel cover">
    <div class="brand-mark cover"><i></i>Willow Lane Therapy</div>
    <svg class="wave" style="top:150px" height="480" viewBox="0 0 380 480">
      <path d="M380 0 Q200 60 60 140 L380 140Z" fill="var(--aqua-soft)" opacity=".6"/>
      <path d="M0 470 Q200 420 380 300 L380 340 Q220 440 0 480Z" fill="var(--teal)"/>
    </svg>
    <div class="cover-photo" role="img" aria-label="Photo of a smiling therapist with a stethoscope holding a young girl"></div>
    <div class="title-pill">
      <h1>Pediatric Occupational<br>Therapy Services</h1>
      <p>(In home services)</p>
    </div>
    <div class="cover-contact">
      <strong>To schedule an appointment,</strong><br>
      call (555) 014-2298<br>
      Email hello@willowlanetherapy.com
    </div>
  </section>

</main>
</body>
</html>
```